Redesign of an educational Eye website for Medical Students and Healthcare professionals

www.corvantisportal.com is an educational resource, illustrated using high quality 3D animations, for undergraduate medical students and healthcare professionals to learn about the anatomy of the human eye and associated common eye disorders.

The website was originally developed (using a Joomla template) a couple of years ago and we now want to update the brand and design of the site. Example content and animations can be found at https://www.corvantisportal.com/overview or https://www.corvantisportal.com/ocular-anatomy/orbital-anatomy

We would like a new logo and home page design (to include new colour palette, fonts and updated overall design).

The attached PowerPoint contains an example layout of the revised components we want to appear on the new Home page. We plan to have a hero panel at the top of page playing a short video of some of the animations. Similar to how this site works (www.zembri.uk.com).

We want the new site to feel Professional, Modern and Clean and simple.

Target Market(s)

Undergraduate medical students and Healthcare Professionals

Industry/Entity Type

Medical

Logo Text

Corvantis Portal

Number of Pages Required

1 page

Font styles to use
Sans Serif

Colors

Designer to choose colors to be used in the design.

```html
<!DOCTYPE html>
<html lang="en">
<head>
<meta charset="utf-8">
<title>Corvantis Portal — Learn Faster and Smarter</title>
<link href="https://fonts.googleapis.com/css2?family=Khand:wght@500;600&family=Open+Sans:wght@400;600;700&display=swap" rel="stylesheet">
<style>
:root{
  --blue:#1d4aa8;
  --red:#e8222f;
  --navy:#1b3566;
  --card-blue:#0d4fa0;
  --cyan:#1ea8e0;
  --ink:#222;
  --muted:#666;
  --light:#eeeeee;
  --white:#fff;
  --grad:linear-gradient(100deg,#1946a8 0%,#5a3f96 50%,#e8222f 100%);
}
*{box-sizing:border-box;margin:0;padding:0}
html,body{width:1200px;height:4478px;overflow:hidden}
body{font-family:"Open Sans",Arial,sans-serif;color:var(--ink);background:var(--white);position:relative}
.heading{font-family:"Khand",Arial,sans-serif;font-weight:600;text-transform:uppercase;letter-spacing:.5px}
.section-title{font-family:"Khand",Arial,sans-serif;font-weight:600;font-size:34px;text-transform:uppercase;text-align:center;letter-spacing:.5px;color:#1a1a1a}
.title-mark{width:8px;height:8px;border-radius:50%;background:var(--red);margin:10px auto 0}
.title-mark.light{background:var(--white)}
section{position:absolute;left:0;width:1200px}
.abs{position:absolute}
.btn{display:inline-block;font-size:13px;color:var(--white);background:var(--cyan);padding:0 18px;line-height:38px;border-radius:2px;text-align:center}

/* hero */
.hero{top:0;height:672px;background:var(--grad);color:var(--white);overflow:hidden}
.hero-photo{position:absolute;inset:0;background:radial-gradient(ellipse at 62% 40%,rgba(255,255,255,.16),rgba(0,0,0,0) 60%)}
.brand{left:160px;top:48px;display:flex;align-items:center;gap:12px}
.brand-dot{width:34px;height:34px;border-radius:50%;background:var(--white)}
.brand-name{font-family:"Khand",Arial,sans-serif;font-weight:600;font-size:30px;text-transform:uppercase;color:var(--white);letter-spacing:.5px}
.top-nav{right:160px;top:58px;display:flex;align-items:center;gap:8px;font-size:13px}
.social{width:20px;height:20px;border:1.5px solid var(--white);border-radius:50%}
.sign-in{margin-left:20px;display:flex;gap:8px;align-items:center}
.hero-title{top:214px;width:100%;text-align:center;font-size:36px}
.play{left:570px;top:300px;width:60px;height:60px}
.hero-text{top:388px;left:240px;width:720px;text-align:center;font-size:13.5px;line-height:22px}
.hero-actions{top:455px;width:100%;display:flex;justify-content:center;gap:12px}
.hero-actions .btn{width:216px;font-size:12px;line-height:44px}
.btn.outline{background:transparent;border:1.5px solid var(--white)}
.scroll-hint{left:586px;top:568px;width:28px;height:56px;border:2px solid var(--white);border-radius:14px}
.scroll-hint::after{content:"";position:absolute;left:10px;top:34px;width:4px;height:8px;border-radius:2px;background:var(--white)}

/* partners */
.partners{top:672px;height:103px;background:var(--light);display:flex;justify-content:space-between;align-items:center;padding:0 160px}
.partner-badge{width:190px;height:40px;background:#bfbfbf;border-radius:3px}

/* why */
.why{top:775px;height:640px}
.why .section-title{margin-top:62px}
.feature-text{width:330px}
.feature-text h3{font-family:"Khand",Arial,sans-serif;font-weight:600;font-size:18px;text-transform:uppercase;margin-bottom:10px}
.feature-text p{font-size:13px;line-height:20px;color:var(--muted);margin-bottom:12px}
.feature-text li{list-style:none;font-size:12px;line-height:18px;color:var(--cyan)}
.feature-text li::before{content:"- "}
.photo{border-radius:2px}
.eye-photo{left:605px;top:165px;width:330px;height:155px;background:linear-gradient(135deg,#6e2a24,#c95b4f 50,#8b3a32)}
.patient-photo{left:160px;top:325px;width:345px;height:165px;background:linear-gradient(135deg,#b5896f,#6d4b3c)}
.divider{left:160px;top:560px;width:880px;height:1px;background:#ddd}

/* modules */
.modules{top:1415px;height:440px}
.modules .section-title{margin-top:0}
.module-card{top:80px;width:272px;height:290px;color:var(--white);text-align:center}
.module-head{height:145px;background:var(--navy);padding-top:28px}
.module-icon{width:36px;height:36px;border:4px solid var(--white);border-radius:50%;margin:0 auto 20px}
.module-head h3{font-size:18px}
.module-body{height:145px;background:var(--card-blue);padding:18px 26px 0}
.module-body p{font-size:13px;line-height:19px}
.module-body span{display:block;margin-top:22px;font-family:"Khand",Arial,sans-serif;font-weight:600;font-size:14px;text-transform:uppercase}

/* team */
.team{top:1855px;height:520px;background:var(--light)}
.team .section-title{margin-top:65px}
.member{top:140px;width:272px;text-align:center}
.member-photo{height:160px;background:linear-gradient(180deg,#f6f7f9,#dfe4ea)}
.member h3{font-size:15px;margin-top:18px}
.member p{font-size:13px;line-height:19px;color:var(--muted);margin:8px 8px 14px}
.member .btn{width:104px;line-height:38px}

/* testimonial */
.testimonial{top:2375px;height:435px;background:var(--grad);color:var(--white)}
.testimonial .section-title{color:var(--white);margin-top:65px}
.quote-box{left:185px;top:185px;width:835px;height:180px;border:1.5px solid rgba(255,255,255,.85);text-align:center;padding:48px 50px 0}
.quote-box p{font-size:13px;line-height:20px}
.quote-box strong{display:block;margin-top:12px;font-size:12px}
.avatar{left:570px;top:150px;width:60px;height:60px;border-radius:50%;border:3px solid var(--white);background:#c89c84}
.arrow{top:262px;width:28px;height:28px;background:var(--white)}
.arrow.prev{left:171px}.arrow.next{left:1006px}

/* trial */
.trial{top:2810px;height:610px;background:var(--light);text-align:center}
.trial .section-title{margin-top:65px}
.trial-note{font-size:13px;color:var(--muted);margin-top:24px}
.trial .btn{margin-top:18px;width:136px}
.trial-visual{left:357px;top:277px;width:485px;height:260px;background:linear-gradient(120deg,#d9e7ef,#a8c4d6 45%,#e9d3c3)}

/* charity */
.charity{top:3420px;height:235px;text-align:center}
.charity .section-title{margin-top:62px}
.charity p{font-size:13px;line-height:20px;color:var(--muted);width:870px;margin:26px auto 0}
.charity-photo{top:3655px;height:370px;background:linear-gradient(90deg,#d8d8d8,#bdbdbd 60%,#a7a7a7)}

/* footer */
.site-footer{top:4025px;height:453px;background:var(--grad);color:var(--white);font-size:12.5px}
.footer-label{font-family:"Khand",Arial,sans-serif;font-weight:600;font-size:15px;text-transform:uppercase;margin-bottom:14px}
.community{left:160px;top:55px}
.community .socials{display:flex;gap:8px}
.community .social{width:24px;height:24px}
.contact-info{left:355px;top:60px}
.contact-info div{display:flex;align-items:center;gap:10px;margin-bottom:12px}
.newsletter{left:665px;top:55px}
.newsletter form{display:flex;gap:10px}
.newsletter .field{width:255px;height:42px;background:var(--white);color:#999;font-size:12px;padding:13px 12px}
.newsletter .btn{width:110px;line-height:42px}
.link-col{top:222px}
.link-col li{list-style:none;line-height:21px}
.copyright{top:390px;width:100%;text-align:center;font-size:11px}
</style>
</head>
<body>

<section class="hero">
  <div class="hero-photo" role="img" aria-label="Video still of a patient wearing an eye patch with visual field overlay"></div>
  <div class="abs brand"><span class="brand-dot"></span><span class="brand-name">Corvantis Portal</span></div>
  <nav class="abs top-nav">
    <span class="social"></span><span class="social"></span><span class="social"></span><span class="social"></span>
    <span class="sign-in">
      <svg width="14" height="14" viewBox="0 0 14 14"><circle cx="7" cy="4.5" r="3" fill="none" stroke="#fff" stroke-width="1.4"/><path d="M1.5 13c0-3 2.5-5 5.5-5s5.5 2 5.5 5" fill="none" stroke="#fff" stroke-width="1.4"/></svg>Sign in</span>
  </nav>
  <h1 class="abs heading hero-title">Learn Faster and Smarter</h1>
  <svg class="abs play" viewBox="0 0 60 60"><circle cx="30" cy="30" r="28" fill="none" stroke="#fff" stroke-width="2"/><path d="M25 20 L41 30 L25 40 Z" fill="#fff"/></svg>
  <p class="abs hero-text">Corvantis Portal helps undergraduates and healthcare professionals to learn or update their knowledge about the clinically relevant anatomy, ophthalmic examination techniques and common eye disorders of the human eye.</p>
  <div class="abs hero-actions">
    <span class="btn">Undergraduates – Learn more</span>
    <span class="btn outline">Healthcare Professionals – Learn more</span>
  </div>
  <div class="abs scroll-hint"></div>
</section>

<section class="partners" aria-label="Partner institutions">
  <span class="partner-badge"></span><span class="partner-badge"></span><span class="partner-badge"></span><span class="partner-badge"></span>
</section>

<section class="why">
  <h2 class="section-title">Why Corvantis Portal ?</h2>
  <div class="title-mark"></div>
  <div class="abs feature-text" style="left:268px;top:180px">
    <h3>Credible</h3>
    <p>Lorem ipsum dolor sit amet, consectetur adipiscing elit, sed do eiusmod tempor incididunt.</p>
    <ul><li>Lorem ipsum dolor sit amet, consectetur adipiscing elit.</li><li>Ut enim ad minim veniam, quis nostrud</li><li>aute in culpa qui officia deserunt mollit anim id est laborum.</li></ul>
  </div>
  <div class="abs photo eye-photo" role="img" aria-label="Close-up photograph of a red, irritated eye"></div>
  <div class="abs photo patient-photo" role="img" aria-label="Photograph of a patient during an eye examination"></div>
  <div class="abs feature-text" style="left:620px;top:350px">
    <h3>Visual</h3>
    <p>Lorem ipsum dolor sit amet, consectetur adipiscing elit, sed do eiusmod tempor incididunt.</p>
    <ul><li>Lorem ipsum dolor sit amet, consectetur adipiscing elit.</li><li>Ut enim ad minim veniam, quis nostrud</li><li>aute in culpa qui officia deserunt mollit anim id est laborum.</li></ul>
  </div>
  <div class="abs divider"></div>
</section>

<section class="modules">
  <h2 class="section-title">Training Modules</h2>
  <div class="title-mark"></div>
  <article class="abs module-card" style="left:163px">
    <div class="module-head"><div class="module-icon"></div><h3 class="heading">Core Principles</h3></div>
    <div class="module-body"><p>Lorem ipsum dolor sit amet, consectetur adipiscing elit, sed do eiusmod tempor incididunt ut labore</p><span>Learn more</span></div>
  </article>
  <article class="abs module-card" style="left:464px">
    <div class="module-head"><div class="module-icon"></div><h3 class="heading">Ophthalmology in Practice</h3></div>
    <div class="module-body"><p>Lorem ipsum dolor sit amet, consectetur adipiscing elit, sed do eiusmod tempor incididunt ut labore</p><span>Learn more</span></div>
  </article>
  <article class="abs module-card" style="left:765px">
    <div class="module-head"><div class="module-icon"></div><h3 class="heading">An Other</h3></div>
    <div class="module-body"><p>Lorem ipsum dolor sit amet, consectetur adipiscing elit, sed do eiusmod tempor incididunt ut labore</p><span>Learn more</span></div>
  </article>
</section>

<section class="team">
  <h2 class="section-title">Meet the Team</h2>
  <div class="title-mark"></div>
  <article class="abs member" style="left:163px">
    <div class="member-photo" role="img" aria-label="Portrait of a male doctor"></div>
    <h3 class="heading">Aldo Marren</h3>
    <p>Lorem ipsum dolor sit amet, consectetur adipiscing elit, sed do eiusmod tempor incididunt ut labore</p>
    <span class="btn">Learn more</span>
  </article>
  <article class="abs member" style="left:464px">
    <div class="member-photo" role="img" aria-label="Portrait of a female doctor at a laptop"></div>
    <h3 class="heading">Lusia Brent</h3>
    <p>Lorem ipsum dolor sit amet, consectetur adipiscing elit, sed do eiusmod tempor incididunt ut labore</p>
    <span class="btn">Learn more</span>
  </article>
  <article class="abs member" style="left:765px">
    <div class="member-photo" role="img" aria-label="Portrait of a man in a suit"></div>
    <h3 class="heading">Teo Varga</h3>
    <p>Lorem ipsum dolor sit amet, consectetur adipiscing elit, sed do eiusmod tempor incididunt ut labore</p>
    <span class="btn">Learn more</span>
  </article>
</section>

<section class="testimonial">
  <h2 class="section-title">What are people saying about Corvantis Portal?</h2>
  <div class="title-mark light"></div>
  <div class="abs quote-box">
    <p>Lorem ipsum dolor sit amet, consectetur adipiscing elit, sed do eiusmod tempor incididunt ut labore et dolore magna aliqua. Ut enim ad minim veniam, quis nostrud exercitation ullamco laboris nisi ut aliquip ex ea commodo consequat. Duis aute irure dolor in reprehenderit in voluptate velit esse cillum dolore eu fugiat nulla pariatur.</p>
    <strong>Jenna Dove</strong>
  </div>
  <div class="abs avatar" role="img" aria-label="Portrait of the reviewer"></div>
  <svg class="abs arrow prev" viewBox="0 0 28 28"><rect width="28" height="28" fill="#fff"/><path d="M16 9 L11 14 L16 19 Z" fill="#222"/></svg>
  <svg class="abs arrow next" viewBox="0 0 28 28"><rect width="28" height="28" fill="#fff"/><path d="M12 9 L17 14 L12 19 Z" fill="#222"/></svg>
</section>

<section class="trial">
  <h2 class="section-title">Want to try Corvantis Portal for free?</h2>
  <div class="title-mark"></div>
  <p class="trial-note">No Credit Card Details Required. It's Completely Free For 3 Days.</p>
  <span class="btn">Start Free Trial</span>
  <div class="abs trial-visual" role="img" aria-label="Digital illustration of an eye with a scanning interface"></div>
</section>

<section class="charity">
  <h2 class="section-title">We give 10% of our profit to charity</h2>
  <div class="title-mark"></div>
  <p>Lorem ipsum dolor sit amet, consectetur adipiscing elit, sed do eiusmod tempor incididunt ut labore et dolore magna aliqua. Ut enim ad minim veniam, quis nostrud exercitation ullamco laboris nisi ut aliquip ex ea commodo consequat.</p>
</section>
<section class="charity-photo" role="img" aria-label="Greyscale photograph of an elderly man covering one eye"></section>

<footer class="abs site-footer" style="left:0;width:1200px">
  <div class="abs community">
    <div class="footer-label">Community</div>
    <div class="socials"><span class="social"></span><span class="social"></span><span class="social"></span><span class="social"></span></div>
  </div>
  <div class="abs contact-info">
    <div><svg width="12" height="16" viewBox="0 0 12 16"><path d="M6 0C2.7 0 0 2.6 0 5.9 0 10 6 16 6 16s6-6 6-10.1C12 2.6 9.3 0 6 0z" fill="#fff"/><circle cx="6" cy="6" r="2.2" fill="#4a3f9a"/></svg>Lorem Ipsum Dolor Sit Amet Consectetur</div>
    <div><svg width="14" height="10" viewBox="0 0 14 10"><rect width="14" height="10" fill="#fff"/><path d="M0 0 L7 6 L14 0" fill="none" stroke="#4a3f9a" stroke-width="1.3"/></svg>info@corvantisportal.com</div>
    <div><svg width="14" height="14" viewBox="0 0 14 14"><path d="M3 0 L5.5 3.5 4 5.2C5 7.3 6.7 9 8.8 10L10.5 8.5 14 11 12.3 14C6 13.5.5 8 0 1.7Z" fill="#fff"/></svg>0312 555 014</div>
  </div>
  <div class="abs newsletter">
    <div class="footer-label">Newsletter</div>
    <form><span class="field">Enter Your Email</span><span class="btn">Subscribe</span></form>
  </div>
  <div class="abs link-col" style="left:160px"><div class="footer-label">Products</div><ul><li>Employee Management</li><li>Employee Effectiveness</li><li>Employee Experience</li><li>Plans &amp; Pricing</li></ul></div>
  <div class="abs link-col" style="left:470px"><div class="footer-label">Resources</div><ul><li>Blogs</li></ul></div>
  <div class="abs link-col" style="left:700px"><div class="footer-label">Company</div><ul><li>Our Story</li><li>Customers</li><li>Careers</li></ul></div>
  <div class="abs link-col" style="left:940px"><div class="footer-label">Contact Us</div><ul><li>Email Sales</li><li>Email Support</li></ul></div>
  <p class="abs copyright">Copyright © 2017 Corvantis Portal. All Rights Reserved</p>
</footer>

</body>
</html>
```